Graphic Design Vendora Book Description

There is a book on Vendora that is my competitor that has a large graphic design as part of the description for the book and I want a similar thing for my book to make it stand out more.

My competitors book is here: https://www.vendora-shop.example/Tidal-Lore-Starters-Grasping-Overview/dp/K31RTWP704/

My book is here: https://www.vendora-shop.example/Tidal-Lore-Groundwork-Workings-Interlacing/dp/K7Q2FXH58C/

You can see the kind of thing I am looking for on the book listing but I have attached an image below.

Thanks

Colin

```html
<!DOCTYPE html>
<html lang="en">
<head>
<meta charset="UTF-8">
<title>Tidal Lore – Book Cover</title>
<link rel="stylesheet" href="https://fonts.googleapis.com/css2?family=Poppins:wght@500;600&family=Montserrat:wght@600;700&display=swap">
<style>
  :root {
    --page-bg: #d9dde3;
    --cover-bg: #0b0f17;
    --cover-edge: #151b26;
    --title-yellow: #e4ef4c;
    --subtitle-cyan: #a8e6ff;
    --glow-core: #e9f6ff;
    --glow-mid: #4aa8ff;
    --glow-outer: rgba(20, 70, 160, 0);
  }
  * { box-sizing: border-box; margin: 0; padding: 0; }
  html, body {
    width: 1200px;
    height: 1200px;
    overflow: hidden;
    background: var(--page-bg);
  }
  .stage {
    width: 1200px;
    height: 1200px;
    display: flex;
    align-items: center;
    justify-content: center;
  }
  .book-cover {
    position: relative;
    width: 640px;
    height: 980px;
    background: var(--cover-bg);
    border-left: 14px solid var(--cover-edge);
    display: flex;
    flex-direction: column;
    align-items: center;
    text-align: center;
    padding: 56px 40px 60px;
  }
  .cover-title {
    font-family: "Poppins", sans-serif;
    font-weight: 600;
    color: var(--title-yellow);
    font-size: 104px;
    line-height: 0.98;
    letter-spacing: 2px;
    text-transform: uppercase;
  }
  .cover-subtitle {
    margin-top: 22px;
    font-family: "Montserrat", sans-serif;
    font-weight: 600;
    color: var(--subtitle-cyan);
    font-size: 22px;
    line-height: 1.2;
    text-transform: uppercase;
  }
  .wave-illustration {
    margin-top: 30px;
    width: 440px;
    height: 380px;
    border-radius: 50%;
    background: radial-gradient(ellipse at center,
      var(--glow-core) 0%,
      var(--glow-mid) 14%,
      rgba(40, 110, 220, 0.45) 38%,
      var(--glow-outer) 70%);
  }
  .cover-tagline {
    margin-top: 36px;
    font-family: "Montserrat", sans-serif;
    font-weight: 600;
    color: var(--subtitle-cyan);
    font-size: 22px;
    line-height: 1.2;
    text-transform: uppercase;
  }
  .cover-author {
    margin-top: auto;
    font-family: "Montserrat", sans-serif;
    font-weight: 700;
    color: var(--title-yellow);
    font-size: 34px;
    letter-spacing: 1px;
    text-transform: uppercase;
  }
</style>
</head>
<body>
  <main class="stage">
    <article class="book-cover">
      <h1 class="cover-title">Tidal<br>Lore</h1>
      <p class="cover-subtitle">The Groundwork of Currents,<br>Interlacing,<br>and Swell Theory</p>
      <div class="wave-illustration" role="img" aria-label="Glowing blue orb with bright core and light trails on crossing orbits"></div>
      <p class="cover-tagline">A Starters Guide to Tidal<br>Workings, Drift, Basin Theory,<br>and Shoreline Mapping</p>
      <p class="cover-author">Elias Thornbury</p>
    </article>
  </main>
</body>
</html>
```